National Virtual CPA Firm needs post card design

Virtual CPA firm called "BRELLVO" needs a 5.5” x 8.5” post card designed to market our services to middle market mid-size american businesses. We provide Full Service Payroll (includes the processing of payroll, printing of checks and direct depositing, tax filing, and tax payments), Bookkeeping (Using their native systems, or ours), Contract CFO (with expense reduction analysis), Reporting services for business directors to make informed decisions, Capital Fundraising (Advice on seeking equity to help grow your business), and Taxes (Personal (1040), Partnership (1065), Corporate (1120, 1120S (Including Consolidated Returns)), Trust (1041) and Non-Profit (990)), including all affiliated state returns. One of our major selling points is our variety of experience, and our fast turn around times on projects.
This project specifically, I would like to highlight the bookkeeping services, but still want the tax and payroll services listed on the postcard.
I have uploaded the logo design for BRELLVO and would like a postcard that compliments the logo.
Company contact info is:
Brellvo accounting services Inc
P.O. Box 4638
Great falls, MT 59172
(800) 613-2794
Www.brellvo-example.com
Target Market(s)
Small to medium size businesses
Industry/Entity Type
Accounting
Look and feel

```html
<!DOCTYPE html>
<html lang="en">
<head>
<meta charset="utf-8">
<title>BRELLVO Postcard</title>
<link href="https://fonts.googleapis.com/css2?family=Montserrat:wght@400;500;600;700;800&display=swap" rel="stylesheet">
<style>
:root{
  --green:#4fb748;
  --yellow:#ffc90b;
  --black:#0b0b0b;
  --ink:#2b2b2b;
  --paper:#ffffff;
  --paper-soft:#f3f3f3;
  --backdrop:#cfcfcf;
}
*{margin:0;padding:0;box-sizing:border-box}
html,body{width:1200px;height:2602px;overflow:hidden}
body{background:linear-gradient(#bdbdbd,#dedede);font-family:"Montserrat",sans-serif;color:var(--ink);position:relative}
.card{position:absolute;left:126px;width:948px;height:614px;background:var(--paper);box-shadow:0 18px 24px rgba(0,0,0,.35);overflow:hidden}
.card-front{top:620px;background:linear-gradient(135deg,var(--paper-soft),#fff 60%)}
.card-back{top:1368px}
.shapes{position:absolute;inset:0}
.brand{position:absolute;display:flex;align-items:center;gap:12px;font-weight:800;color:var(--black);letter-spacing:1px}
.brand-dot{width:22px;height:22px;border-radius:50%;background:var(--yellow)}
.front-brand{left:32px;top:62px;font-size:46px}
.headline{position:absolute;left:28px;top:196px;color:#fff;line-height:1.12}
.headline .small{font-size:24px;font-weight:400}
.headline .green{font-size:40px;font-weight:700;color:var(--green)}
.headline .mid{font-size:27px;font-weight:600}
.headline .mid .light{font-weight:400}
.headline .yellow{font-size:40px;font-weight:700;color:var(--yellow)}
.services{position:absolute;top:422px;font-size:14px;line-height:28px}
.services b{font-weight:600}
.services .arrow{color:var(--green);font-weight:700;margin-right:4px}
.services-left{left:26px}
.services-right{left:206px;line-height:20px}
.services-right li{margin-bottom:13px;padding-left:16px;text-indent:-16px}
.services li{list-style:none}
.contact-title{position:absolute;left:22px;top:530px;font-size:14px;font-weight:600;color:var(--green);display:flex;align-items:center;gap:6px;width:455px}
.contact-title::after{content:"";flex:1;height:1px;background:#777}
.contact-row{position:absolute;left:22px;top:552px;display:flex;align-items:center;font-size:14px;line-height:19px}
.ic{width:20px;height:20px;flex:none}
.contact-row .addr{margin:0 10px 0 8px;padding-right:10px;border-right:1px solid #555}
.contact-row .web{margin-left:6px}
.contact-row .web b,.back-footer b{color:var(--green);font-weight:500}
.phone-band{position:absolute;left:565px;top:540px;display:flex;align-items:center;gap:10px;color:#fff;font-size:36px;font-weight:700}
.back-heading{position:absolute;left:105px;top:122px;width:240px;height:36px;background:var(--yellow);border-radius:8px;transform:skewX(-12deg);display:flex;align-items:center;justify-content:center}
.back-heading span{transform:skewX(12deg);font-size:21px;font-weight:700;color:var(--black)}
.offer-list{position:absolute;left:24px;top:180px;color:#fff;list-style:none}
.offer-list li{display:flex;gap:18px;margin-bottom:18px;font-size:14px;line-height:19px}
.offer-list .badge{width:44px;height:44px;border-radius:50%;background:var(--yellow);border:3px solid #fff3b0;flex:none;display:flex;align-items:center;justify-content:center;margin-top:4px}
.offer-list b{font-weight:600;display:block}
.back-brand{left:542px;top:74px;font-size:34px}
.stamp{position:absolute;left:785px;top:42px;width:110px;height:110px;border:1px solid #333}
.address-line{position:absolute;left:570px;width:326px;height:1px;background:#333}
.back-footer{position:absolute;left:24px;top:552px;display:flex;align-items:center;gap:8px;font-size:16px}
.back-footer .tel{font-weight:700;padding-right:10px;border-right:1px solid #333}
</style>
</head>
<body>

<section class="card card-front">
  <svg class="shapes" viewBox="0 0 948 614" width="948" height="614">
    <path d="M352 162 H420 Q444 164 436 188 L382 372 Q376 392 352 392 Z" fill="var(--yellow)"/>
    <path d="M0 158 H406 Q428 158 422 180 L368 368 Q362 388 340 388 H0 Z" fill="var(--black)"/>
    <path d="M502 65 H902 Q922 65 918 85 L874 388 Q870 408 850 408 H447 Q427 408 430 388 L484 85 Q488 65 502 65 Z" fill="var(--green)"/>
    <path d="M492 109 H892 Q912 109 908 129 L864 432 Q860 452 840 452 H437 Q417 452 420 432 L474 129 Q478 109 492 109 Z" fill="var(--yellow)"/>
    <path d="M480 87 H880 Q900 87 896 107 L852 410 Q848 430 828 430 H425 Q405 430 408 410 L462 107 Q466 87 480 87 Z" fill="url(#photoTone)" role="img" aria-label="Photo of a smiling accountant in a suit reviewing documents at an office desk with charts on a monitor"/>
    <defs>
      <linearGradient id="photoTone" x1="0" y1="0" x2="1" y2="1">
        <stop offset="0" stop-color="#dfe6ee"/>
        <stop offset=".55" stop-color="#9aa4b8"/>
        <stop offset="1" stop-color="#2b3450"/>
      </linearGradient>
    </defs>
    <path d="M522 515 H548 L500 614 H474 Z" fill="var(--yellow)"/>
    <path d="M560 515 H948 V614 H512 Z" fill="var(--green)"/>
  </svg>

  <div class="brand front-brand"><span class="brand-dot"></span>BRELLVO</div>

  <h1 class="headline">
    <span class="small">Variety of</span><br>
    <span class="green">experience,</span><br>
    <span class="mid"><span class="light">and</span> our fast turn around</span><br>
    <span class="mid">times on</span> <span class="yellow">projects.</span>
  </h1>

  <ul class="services services-left">
    <li><span class="arrow">»</span><b>Taxes</b> (Personal (1040)</li>
    <li><span class="arrow">»</span><b>Trust</b> (1041)</li>
    <li><span class="arrow">»</span><b>Partnership</b> (1065)</li>
  </ul>
  <ul class="services services-right">
    <li><span class="arrow">»</span><b>Non-Profit</b> (990), including<br>all affiliated state returns.</li>
    <li><span class="arrow">»</span><b>Corporate</b> (1120, 1120S)<br>(Including Consolidated Returns)</li>
  </ul>

  <div class="contact-title">Contact Info</div>
  <div class="contact-row">
    <svg class="ic" viewBox="0 0 20 20"><circle cx="10" cy="10" r="9" fill="none" stroke="var(--green)" stroke-width="1.3"/><path d="M10 4.5a3.3 3.3 0 0 0-3.3 3.3c0 2.5 3.3 6.6 3.3 6.6s3.3-4.1 3.3-6.6A3.3 3.3 0 0 0 10 4.5z" fill="var(--green)"/><circle cx="10" cy="7.8" r="1.2" fill="#fff"/></svg>
    <span class="addr">Brellvo accounting services Inc<br>P.O. Box 4638, Great falls, MT 59172</span>
    <svg class="ic" viewBox="0 0 20 20"><circle cx="10" cy="10" r="9" fill="none" stroke="var(--green)" stroke-width="1.3"/><circle cx="10" cy="10" r="5.5" fill="none" stroke="var(--green)"/><path d="M4.5 10h11M10 4.5c-2.5 3-2.5 8 0 11M10 4.5c2.5 3 2.5 8 0 11" fill="none" stroke="var(--green)" stroke-width=".8"/></svg>
    <span class="web">www.<b>brellvo-example</b>.com</span>
  </div>

  <div class="phone-band">
    <svg width="30" height="30" viewBox="0 0 24 24"><path d="M6.6 10.8a15 15 0 0 0 6.6 6.6l2.2-2.2a1 1 0 0 1 1-.25 11.4 11.4 0 0 0 3.6.57 1 1 0 0 1 1 1V20a1 1 0 0 1-1 1A17 17 0 0 1 3 4a1 1 0 0 1 1-1h3.5a1 1 0 0 1 1 1c0 1.25.2 2.45.57 3.57a1 1 0 0 1-.25 1z" fill="#fff"/><path d="M14 3a7 7 0 0 1 7 7M14 6.5a3.5 3.5 0 0 1 3.5 3.5" stroke="#fff" stroke-width="1.6" fill="none"/></svg>
    (800) 613-2794
  </div>
</section>

<section class="card card-back">
  <svg class="shapes" viewBox="0 0 948 614" width="948" height="614">
    <path d="M440 96 H470 Q498 98 490 126 L400 486 Q392 517 360 517 H330 Z" fill="var(--yellow)"/>
    <path d="M0 96 H450 Q478 96 470 124 L380 486 Q372 517 340 517 H0 Z" fill="var(--green)"/>
  </svg>

  <div class="back-heading"><span>What We provide</span></div>

  <ul class="offer-list">
    <li><span class="badge"><svg width="22" height="22" viewBox="0 0 24 24"><rect x="3" y="9" width="18" height="11" rx="2" fill="none" stroke="#333" stroke-width="1.6"/><circle cx="12" cy="14.5" r="2.5" fill="none" stroke="#333" stroke-width="1.4"/><path d="M6 7l5-4 3 3 4-3" fill="none" stroke="#333" stroke-width="1.4"/></svg></span>
      <p><b>Payroll</b>(includes the processing of payroll,<br>printing of checks and direct depositing,<br>tax filing, and tax payments).</p></li>
    <li><span class="badge"><svg width="22" height="22" viewBox="0 0 24 24"><rect x="5" y="3" width="14" height="18" rx="2" fill="none" stroke="#333" stroke-width="1.6"/><path d="M8 8h8M8 12h8M8 16h5" stroke="#333" stroke-width="1.4"/></svg></span>
      <p><b>Bookkeeping</b>(Using their native systems, or ours).</p></li>
    <li><span class="badge"><svg width="22" height="22" viewBox="0 0 24 24"><rect x="4" y="3" width="13" height="17" rx="2" fill="none" stroke="#333" stroke-width="1.6"/><path d="M7 8h7M7 12h7" stroke="#333" stroke-width="1.4"/><path d="M12 18l3 3 6-6" fill="none" stroke="#333" stroke-width="1.6"/></svg></span>
      <p><b>Contract CFO</b>(with expense reduction analysis),<br>Reporting services for business directors<br>to make informed decisions.</p></li>
    <li><span class="badge"><svg width="22" height="22" viewBox="0 0 24 24"><circle cx="12" cy="9" r="6" fill="none" stroke="#333" stroke-width="1.6"/><path d="M12 5.5v7M10 7.5h3a1.2 1.2 0 0 1 0 2.4h-2a1.2 1.2 0 0 0 0 2.4h3" fill="none" stroke="#333" stroke-width="1.2"/><path d="M3 20c3-3 6-3 9-1s6 2 9-1" fill="none" stroke="#333" stroke-width="1.6"/></svg></span>
      <p><b>Capital Fundraising</b>(Advice on seeking equity to help<br>grow your business)</p></li>
  </ul>

  <div class="brand back-brand"><span class="brand-dot"></span>BRELLVO</div>
  <div class="stamp"></div>
  <div class="address-line" style="top:306px"></div>
  <div class="address-line" style="top:384px"></div>
  <div class="address-line" style="top:462px"></div>

  <div class="back-footer">
    <svg class="ic" viewBox="0 0 20 20"><circle cx="10" cy="10" r="9" fill="none" stroke="var(--green)" stroke-width="1.3"/><path d="M6.5 5.5h2l1 2.5-1.2 1a6 6 0 0 0 2.7 2.7l1-1.2 2.5 1v2a1 1 0 0 1-1 1A8 8 0 0 1 5.5 6.5a1 1 0 0 1 1-1z" fill="var(--green)"/></svg>
    <span class="tel">(800) 613-2794</span>
    <svg class="ic" viewBox="0 0 20 20"><circle cx="10" cy="10" r="9" fill="none" stroke="var(--green)" stroke-width="1.3"/><circle cx="10" cy="10" r="5.5" fill="none" stroke="var(--green)"/><path d="M4.5 10h11M10 4.5c-2.5 3-2.5 8 0 11M10 4.5c2.5 3 2.5 8 0 11" fill="none" stroke="var(--green)" stroke-width=".8"/></svg>
    <span>www.<b>brellvo-example</b>.com</span>
  </div>
</section>

</body>
</html>
```